Copper Meadow Packaging Design for RTE Beans

We need a product mock design that is aligned with our brand image. We need three SKUs. Black bean, Pinto bean, and Chickpeas. I've uploaded our brand logo here, Copper Meadow. I have also took a screenshot of the design elements that we would like to see. The packaging die line can be seen on the file "packaging sample". Please refer to the screenshots for packaging design directions.

```html
<!DOCTYPE html>
<html lang="en">
<head>
<meta charset="utf-8">
<title>Copper Meadow – Black Bean Pouch</title>
<link href="https://fonts.googleapis.com/css2?family=Rye&family=Alfa+Slab+One&family=Old+Standard+TT:wght@400;700&display=swap" rel="stylesheet">
<style>
  :root {
    --backdrop: #ececec;
    --kraft: #857a62;
    --kraft-dark: #6c6250;
    --kraft-speck: #a49a82;
    --label: #ebe3c6;
    --label-shade: #d9cfae;
    --ink: #38322c;
    --bean-green: #4f6b2d;
    --banner: #2a2624;
    --banner-text: #efe6cc;
    --bean-dark: #15141b;
    --bean-mid: #2d2c39;
    --figure: #9a937f;
  }
  * { margin: 0; padding: 0; box-sizing: border-box; }
  html, body {
    width: 1200px;
    height: 1200px;
    overflow: hidden;
    background: var(--backdrop);
  }
  .canvas { position: relative; width: 1200px; height: 1200px; }
  .pouch {
    position: absolute;
    left: 274px;
    top: 152px;
    width: 652px;
    height: 916px;
    border-radius: 6px 6px 10px 10px;
    overflow: hidden;
    background:
      radial-gradient(circle at 22% 8%, rgba(164,154,130,.55) 0 2px, transparent 3px),
      radial-gradient(circle at 78% 5%, rgba(164,154,130,.5) 0 2px, transparent 3px),
      radial-gradient(circle at 60% 9%, rgba(164,154,130,.45) 0 1.5px, transparent 2.5px),
      linear-gradient(180deg, var(--kraft) 0%, var(--kraft-dark) 100%);
    box-shadow: 0 14px 26px rgba(0,0,0,.12);
  }
  .label-sheet {
    position: absolute;
    left: 0; top: 0;
    width: 652px; height: 916px;
  }
  .mascot-art {
    position: absolute;
    left: 254px; top: 162px;
    width: 168px; height: 226px;
    background: radial-gradient(ellipse at 50% 42%, #b8b19f 0%, var(--figure) 60%, rgba(154,147,127,0) 100%);
    border-radius: 50% 50% 14px 14px;
    opacity: .8;
  }
  .brand-name {
    position: absolute;
    left: 0; width: 100%;
    top: 404px;
    text-align: center;
    white-space: nowrap;
    font-family: "Rye", serif;
    font-size: 38px;
    letter-spacing: 1px;
    color: var(--ink);
    line-height: 1;
  }
  .bean-window {
    position: absolute;
    left: 168px; top: 496px;
    width: 326px; height: 138px;
    background: radial-gradient(ellipse at 40% 40%, var(--bean-mid) 0%, var(--bean-dark) 78%);
    clip-path: polygon(1% 4%, 20% 0, 48% 3%, 76% 0, 99% 3%, 100% 45%, 98% 97%, 70% 100%, 40% 97%, 12% 100%, 0 96%, 2% 50%);
  }
  .product-name {
    position: absolute;
    left: 0; width: 100%;
    top: 650px;
    text-align: center;
    white-space: nowrap;
    font-family: "Alfa Slab One", serif;
    font-weight: 400;
    font-size: 52px;
    letter-spacing: 1px;
    color: var(--bean-green);
    line-height: 1.3;
  }
  .flavour-banner {
    position: absolute;
    left: 112px; top: 738px;
    width: 440px; height: 44px;
    background: var(--banner);
    border-radius: 22px 6px 22px 6px;
    display: flex;
    align-items: center;
    justify-content: center;
    white-space: nowrap;
    font-family: "Old Standard TT", serif;
    font-weight: 700;
    font-size: 18px;
    letter-spacing: .6px;
    color: var(--banner-text);
  }
  .facts-row {
    position: absolute;
    left: 0; width: 100%;
    top: 800px;
    display: flex;
    justify-content: center;
    align-items: center;
    gap: 14px;
    font-family: "Old Standard TT", serif;
    font-weight: 700;
    color: var(--ink);
  }
  .fact { font-size: 14px; line-height: 1.35; white-space: nowrap; }
  .fact-claims { text-align: right; }
  .fact-weight { text-align: left; }
  .heat-level {
    font-family: "Alfa Slab One", serif;
    font-size: 30px;
    line-height: 1;
  }
  .divider { width: 2px; height: 48px; background: var(--ink); }
</style>
</head>
<body>
<main class="canvas">
  <section class="pouch">
    <svg class="label-sheet" viewBox="0 0 652 916" aria-hidden="true">
      <defs>
        <filter id="rough-edge" x="-5%" y="-5%" width="110%" height="110%">
          <feTurbulence type="fractalNoise" baseFrequency="0.045" numOctaves="3" seed="7" result="noise"/>
          <feDisplacementMap in="SourceGraphic" in2="noise" scale="22" xChannelSelector="R" yChannelSelector="G"/>
        </filter>
        <filter id="paper-grain">
          <feTurbulence type="fractalNoise" baseFrequency="0.9" numOctaves="2" seed="3"/>
          <feColorMatrix values="0 0 0 0 0.45  0 0 0 0 0.4  0 0 0 0 0.3  0 0 0 0.18 0"/>
          <feComposite in2="SourceGraphic" operator="in"/>
        </filter>
        <radialGradient id="label-fill" cx="50%" cy="45%" r="65%">
          <stop offset="0%" stop-color="#efe8cd"/>
          <stop offset="80%" stop-color="#e6dcbd"/>
          <stop offset="100%" stop-color="#d3c8a5"/>
        </radialGradient>
      </defs>
      <g filter="url(#rough-edge)">
        <rect x="56" y="124" width="540" height="772" fill="url(#label-fill)"/>
        <rect x="56" y="124" width="540" height="772" fill="#000" filter="url(#paper-grain)"/>
      </g>
    </svg>
    <div class="mascot-art" role="img" aria-label="Illustration of the brand mascot in a sombrero holding wheat stalks"></div>
    <div class="brand-name">COPPER MEADOW</div>
    <div class="bean-window" role="img" aria-label="Photo of dry black beans"></div>
    <h1 class="product-name">BLACK BEAN</h1>
    <div class="flavour-banner">WHIT ONIONS AND BELL PEPPER</div>
    <div class="facts-row">
      <div class="fact fact-claims">NON-GMO<br>PLANT PROTEIN</div>
      <span class="divider"></span>
      <div class="heat-level">MILD</div>
      <span class="divider"></span>
      <div class="fact fact-weight">NET.WT.<br>10 OZ (283 G)</div>
    </div>
  </section>
</main>
</body>
</html>
```